'Tarvel' a financial/crypto-currency exchange in the middle east

On the card we need 1) Name 2) title 3) email address 4) phone number using the same colors and theme as the logo. On one side we just want the logo and we want the whole card to be in blue (same blue as logo) with the logo in the back being white.
Industry/Entity Type
Financial

```html
<!DOCTYPE html>
<html lang="en">
<head>
<meta charset="utf-8">
<title>Tarvel Business Card</title>
<link rel="stylesheet" href="https://fonts.googleapis.com/css2?family=Poppins:wght@600&family=Open+Sans:wght@400;600&display=swap">
<style>
  :root {
    --stage: #e9e6e2;
    --brand-blue: #2395d2;
    --ink-blue: #1b8dcc;
    --white: #ffffff;
    --text-grey: #4f5358;
  }
  * { margin: 0; padding: 0; box-sizing: border-box; }
  html, body { width: 1200px; height: 1000px; overflow: hidden; }
  body {
    background: var(--stage);
    position: relative;
    font-family: "Open Sans", Arial, sans-serif;
  }
  .card {
    position: absolute;
    left: 266px;
    width: 666px;
    height: 397px;
    border-radius: 24px;
    overflow: hidden;
  }
  .card--front { top: 74px; background: var(--brand-blue); }
  .card--back { top: 533px; background: var(--white); }

  .brand {
    position: absolute;
    display: flex;
    align-items: center;
  }
  .brand__dot { border-radius: 50%; flex: none; }
  .brand__name {
    font-family: "Poppins", Arial, sans-serif;
    font-weight: 600;
    line-height: 1;
  }
  .card--front .brand { left: 138px; top: 141px; gap: 22px; }
  .card--front .brand__dot { width: 114px; height: 114px; border: 5px solid var(--white); }
  .card--front .brand__name { font-size: 64px; color: var(--white); }

  .card--back .brand { left: 33px; top: 42px; gap: 16px; }
  .card--back .brand__dot { width: 74px; height: 74px; background: var(--ink-blue); }
  .card--back .brand__name { font-size: 42px; color: var(--ink-blue); }

  .feature-disc {
    position: absolute;
    left: 312px;
    top: 36px;
    width: 324px;
    height: 324px;
    border-radius: 50%;
    background: var(--ink-blue);
  }

  .person { position: absolute; left: 34px; top: 150px; }
  .person__name {
    font-weight: 600;
    font-size: 20px;
    color: var(--ink-blue);
    text-transform: uppercase;
    line-height: 1.2;
  }
  .person__title { font-size: 16px; color: var(--text-grey); line-height: 1.4; }

  .contacts { position: absolute; left: 33px; top: 206px; list-style: none; }
  .contacts li {
    display: flex;
    align-items: center;
    gap: 6px;
    font-size: 16px;
    color: var(--text-grey);
    height: 22px;
  }
  .contacts svg { width: 15px; height: 15px; fill: var(--ink-blue); flex: none; }
  .contacts .address { margin-top: 4px; }

  .social {
    position: absolute;
    left: 33px;
    top: 334px;
    display: flex;
    align-items: center;
    gap: 8px;
    font-weight: 600;
    font-size: 16px;
    color: var(--text-grey);
  }
  .social__dot { width: 17px; height: 17px; border-radius: 50%; background: var(--ink-blue); }
</style>
</head>
<body>
  <section class="card card--front">
    <div class="brand">
      <span class="brand__dot"></span>
      <span class="brand__name">Tarvel</span>
    </div>
  </section>

  <section class="card card--back">
    <div class="brand">
      <span class="brand__dot"></span>
      <span class="brand__name">Tarvel</span>
    </div>

    <div class="person">
      <p class="person__name">Nora Halstead</p>
      <p class="person__title">Managing Director</p>
    </div>

    <ul class="contacts">
      <li>
        <svg viewBox="0 0 16 16"><path d="M3 6c0-3 2-4 5-4s5 1 5 4h-3V5H6v1zM2 7h12l-1 7H3z"/></svg>
        + 000 000 000
      </li>
      <li>
        <svg viewBox="0 0 16 16"><path d="M5 1h6a1 1 0 0 1 1 1v12a1 1 0 0 1-1 1H5a1 1 0 0 1-1-1V2a1 1 0 0 1 1-1zm.5 1.5v10h5v-10zM8 13.2a.6.6 0 1 0 0 1.2.6.6 0 0 0 0-1.2z" fill-rule="evenodd"/></svg>
        + 000 000 000
      </li>
      <li>
        <svg viewBox="0 0 16 16"><path d="M1 4h14v9H1zM1.5 4.5 8 9l6.5-4.5v1L8 10 1.5 5.5z" fill-rule="evenodd"/></svg>
        Nora@tarvel.com
      </li>
      <li>
        <svg viewBox="0 0 16 16"><path d="M8 1a7 7 0 1 0 0 14A7 7 0 0 0 8 1zm0 1.5c.8 0 1.8 1.8 2 4.5H6c.2-2.7 1.2-4.5 2-4.5zM2.6 7h2c.1-1.7.5-3.1 1-4a5.5 5.5 0 0 0-3 4zm10.8 0a5.5 5.5 0 0 0-3-4c.5.9.9 2.3 1 4zM2.6 9a5.5 5.5 0 0 0 3 4c-.5-.9-.9-2.3-1-4zm3.4 0c.2 2.7 1.2 4.5 2 4.5s1.8-1.8 2-4.5zm5.4 0c-.1 1.7-.5 3.1-1 4a5.5 5.5 0 0 0 3-4z" fill-rule="evenodd"/></svg>
        www.tarvel.com
      </li>
      <li class="address">215 Cedar Point Rd, FL 33910</li>
    </ul>

    <div class="social">
      <span class="social__dot"></span>
      <span>@Tarvel</span>
    </div>

    <div class="feature-disc"></div>
  </section>
</body>
</html>
```